Web design for a french company scanning and analyzing road infrastructures

Veltrane is a French company specializing in the digitization and advanced analysis of road infrastructures.

The current site consists of a single landing page.

We would now like to expand the site to detail the services we offer.

We would therefore like to have several pages created:
- redesign of the home page
- “traffic intersection” study page: Veltrane offers several studies, so we need to create a template for these studies, using the theme of traffic intersections as an example.
- “horizontal marking” service page: The studies are made up of services (simple post-processing). There will be multiple services. Here too, we need to create a template for these services, with the "horizontal marking " service as an example.

Elements to keep (all of them are available in the links below) :
- The Veltrane logo, which must be kept as is, including colors.
- Existing product and service illustrations and videos.
- Existing texts must be kept as they are, in terms of wording and hierarchy, to guarantee the accuracy of the information provided.
- Links to the current "home" (https://veltrane.example/), "traffic intersection" (https://veltrane.example/etudes/intersection/) and "horizontal marking" (https://veltrane.example/post-traitements/signalisation-horizontale-2-2/ ) pages.

Creative guidelines :
- Elegance: Design should communicate elegance while remaining accessible.
- Modernity and Innovation: Draw inspiration from the latest trends in web design to convey our commitment to innovation.
- Content enhancement: The layout should emphasize textual and visual content in a balanced and harmonious way.

To achieve this, you have the option of changing typography, colors (excluding logo), generic illustrations (i.e. not specific to our products and services), and integrating pictograms as required.

Delivery of files :
- Files must be created in Photoshop or Illustrator.
- They must include mock-ups for smartphone, tablet and PC screen resolutions of 1280px and higher.

```html
<!DOCTYPE html>
<html lang="fr">
<head>
<meta charset="utf-8">
<title>Signalisation Horizontale – Veltrane</title>
<link href="https://fonts.googleapis.com/css2?family=Saira:wght@400;500;600;700&family=Montserrat:wght@400;500&display=swap" rel="stylesheet">
<style>
:root{
  --bg:#0c0c0c;
  --bg-deep:#070707;
  --green:#1ee83c;
  --green-soft:#22d13d;
  --card-top:#0a4417;
  --card-bottom:#062a0d;
  --text:#ffffff;
  --muted:#d6d6d6;
}
*{margin:0;padding:0;box-sizing:border-box}
html,body{width:1200px;height:4405px;overflow:hidden;background:var(--bg);color:var(--text);font-family:"Montserrat",sans-serif}
h1,h2,h3,.heading{font-family:"Saira",sans-serif;font-weight:500}
p{font-size:13.5px;line-height:23.4px;color:var(--muted)}
section,header,footer{position:relative;width:1200px}
a{color:inherit;text-decoration:none}

/* Header */
.site-header{height:103px;background:#0b0b0b}
.brand{position:absolute;left:84px;top:30px;display:flex;align-items:center;gap:12px}
.brand-mark{width:40px;height:40px;background:var(--green);border-radius:8px}
.brand-name{font-family:"Saira",sans-serif;font-weight:700;font-size:38px;line-height:44px;color:var(--green);letter-spacing:1px}
.menu-toggle{position:absolute;left:1070px;top:29px;width:45px;height:45px;background:var(--green);border-radius:4px;display:flex;flex-direction:column;justify-content:center;align-items:center;gap:3px}
.menu-toggle span{width:13px;height:2px;background:#0b3d14}

/* Hero */
.hero{height:442px;background:#0e0e0e;z-index:2}
.hero-visual{position:absolute;right:0;top:0;width:760px;height:442px;background:linear-gradient(90deg,#0e0e0e 0%,rgba(14,14,14,.6) 25%,rgba(14,14,14,0) 55%),linear-gradient(135deg,#3a3a3a,#7a7a7a 40%,#2b2b2b 70%,#555 100%)}
.hero h1{position:absolute;left:84px;top:96px;font-size:52px;line-height:62px}
.hero-text{position:absolute;left:84px;top:182px;width:680px}
.hero-text p{font-size:13px;line-height:23.4px;color:#e8e8e8}
.breadcrumb{position:absolute;left:84px;top:419px;width:262px;height:45px;background:var(--green);border-radius:4px;display:flex;align-items:center;gap:10px;padding-left:18px;font-size:12px;color:#0b3310;font-weight:500;z-index:3}

/* Méthode */
.method{height:926px;background:radial-gradient(circle at 0 10%,rgba(30,232,60,.08),transparent 380px),var(--bg)}
.section-title{text-align:center;font-size:40px;line-height:50px}
.method .section-title{position:absolute;left:0;right:0;top:92px}
.method-cards{position:absolute;left:84px;top:230px;display:flex;gap:26px}
.method-card{position:relative;width:326px;height:597px;border-radius:14px;background:linear-gradient(180deg,var(--card-top),var(--card-bottom));padding:70px 26px 0 24px}
.method-icon{position:absolute;left:24px;top:-39px;width:82px;height:82px;border-radius:12px;background:var(--green);display:flex;align-items:center;justify-content:center}
.method-card h3{font-size:27px;line-height:33px;color:var(--green);margin-bottom:14px}
.method-card p{font-size:13px;line-height:23.4px;color:#e6e6e6}

/* Avantages */
.benefits{height:683px;background:radial-gradient(ellipse at 80% 20%,rgba(30,180,60,.28),transparent 60%),linear-gradient(180deg,#0a2e12,#071a0b 60%,#0b0b0b)}
.benefits h2{position:absolute;left:84px;top:100px;font-size:40px;line-height:50px}
.benefits-text{position:absolute;left:84px;top:170px;width:670px}
.benefits-text p{font-size:13px}
.carousel{position:absolute;left:84px;top:347px;display:flex;gap:26px}
.slide{width:326px}
.slide-visual{height:200px;border-radius:3px}
.slide-caption{margin-top:20px;text-align:center;font-size:13px;line-height:23px;color:#e6e6e6;padding:0 10px}
.carousel-arrow{position:absolute;top:420px;width:52px;height:52px;border-radius:12px;background:var(--green);display:flex;align-items:center;justify-content:center}
.carousel-arrow.prev{left:56px}
.carousel-arrow.next{left:1089px}

/* Études */
.studies{height:462px}
.studies h2{position:absolute;left:0;right:0;top:48px}
.studies-intro{position:absolute;left:84px;right:84px;top:116px;text-align:center}
.studies-intro{font-size:13px}
.study-tiles{position:absolute;left:84px;top:202px;display:flex;gap:25px}
.study-tile{position:relative;width:240px;height:217px;border-radius:12px;overflow:hidden}
.study-tile span{position:absolute;left:0;right:0;bottom:24px;text-align:center;font-family:"Saira",sans-serif;font-size:20px;line-height:26px;font-weight:500}

/* Importance */
.importance{height:769px;background:radial-gradient(circle at 100% 70%,rgba(30,232,60,.08),transparent 400px),var(--bg)}
.importance h2{position:absolute;left:0;right:0;top:56px}
.importance-cols{position:absolute;left:84px;top:149px;display:flex;gap:29px}
.importance-cols div{width:502px}
.importance-cols p{font-size:13px;margin-bottom:23.4px}

/* Autres */
.others{height:530px;background:linear-gradient(180deg,#0b3a14,#082510 55%,#0c0c0c)}
.others h2{position:absolute;left:0;right:0;top:100px}
.others-list{position:absolute;left:84px;top:188px;display:flex;gap:26px}
.other{width:326px;text-align:center}
.other-visual{height:200px}
.other span{display:block;margin-top:22px;font-family:"Saira",sans-serif;font-size:21px;line-height:26px;font-weight:500}

/* Footer */
.site-footer{height:436px;background:var(--bg)}
.footer-brand{position:absolute;left:0;right:0;top:104px;display:flex;justify-content:center;align-items:center;gap:12px}
.footer-cols{position:absolute;left:84px;top:192px;display:flex;gap:26px}
.footer-col{width:326px}
.footer-col h4{font-family:"Saira",sans-serif;font-weight:500;font-size:21px;color:var(--green);margin-bottom:14px}
.footer-col li{list-style:none;font-size:13.5px;line-height:32px;color:#ddd;display:flex;align-items:center;gap:10px}
.nav-split{display:flex;gap:40px}
.nav-split ul:last-child{padding-top:6px}
.bottom-bar{height:55px;background:var(--bg-deep);text-align:center;font-size:13px;line-height:55px;color:#ddd}
.bottom-bar em{font-style:normal;color:var(--green)}
</style>
</head>
<body>

<header class="site-header">
  <a class="brand" href="https://veltrane.example/"><span class="brand-mark"></span><span class="brand-name">Veltrane</span></a>
  <div class="menu-toggle"><span></span><span></span><span></span></div>
</header>

<section class="hero">
  <div class="hero-visual" role="img" aria-label="Vue aérienne lidar d'un carrefour avec passages piétons et points de mesure"></div>
  <h1>Signalisation Horizontale</h1>
  <div class="hero-text">
    <p>À partir du jumeau numérique généré par notre Corevia, nos algorithmes d'intelligence artificielle permettent de détecter et d'évaluer l'état de l'ensemble des éléments de signalisation horizontale sur les voies scannées.<br>En se basant sur l'indice de réflexion du Lidar, notre processus permet de déterminer une surface associée à un indicateur d'état pour l'ensemble des différents marquages au sol.<br>Cet indicateur d'état facilite ensuite la priorisation et la planification des travaux d'entretien et de rénovation de la signalisation horizontale.</p>
  </div>
  <a class="breadcrumb" href="https://veltrane.example/">Home
    <svg width="16" height="12" viewBox="0 0 16 12"><path d="M1 6h13M9 1l5 5-5 5" fill="none" stroke="#0b3310" stroke-width="1.8"/></svg>
    Signalisation Horizontale</a>
</section>

<section class="method">
  <h2 class="section-title">Méthode D'Analyse</h2>
  <div class="method-cards">
    <article class="method-card">
      <div class="method-icon"><svg width="36" height="36" viewBox="0 0 36 36" fill="none" stroke="#fff" stroke-width="2.4" stroke-linecap="round"><path d="M4 11V7a3 3 0 0 1 3-3h4M25 4h4a3 3 0 0 1 3 3v4M32 25v4a3 3 0 0 1-3 3h-4M11 32H7a3 3 0 0 1-3-3v-4"/><rect x="11" y="11" width="14" height="14" rx="4"/><path d="M8 18h20"/></svg></div>
      <h3>Détection et vectorisation de la signalisation horizontale</h3>
      <p>La première étape du processus consiste à détecter la signalisation horizontale à partir des données lidar, créant ainsi une orthophoto-lidar des chaussées et dépendances. Le nuage de points 3D est coupé à une hauteur de 2 mètres pour éliminer les masques potentiels, la couleur provenant principalement de l'intensité de réflexion du lidar.<br>Complémentairement, la caméra est utilisée pour détecter la couleur spécifique des bandes routières.</p>
    </article>
    <article class="method-card">
      <div class="method-icon"><svg width="34" height="36" viewBox="0 0 34 36" fill="none" stroke="#fff" stroke-width="2.4" stroke-linecap="round" stroke-linejoin="round"><rect x="4" y="6" width="26" height="27" rx="5"/><path d="M12 3h10v6H12zM12 20l4 4 7-8"/></svg></div>
      <h3>Inventaire du marquage routier</h3>
      <p>Notre scan permet de réaliser un inventaire détaillé du marquage routier, incluant des relevés par type pour les objets linéaires et ponctuels (flèches de rabattement, flèches tourne-à-gauche, zebra TPC, cédez le passage, etc). Nos algorithmes d'intelligence artificielle entrent en action pour détecter, classifier, et calculer les surfaces associées à différents marquages routiers.</p>
    </article>
    <article class="method-card">
      <div class="method-icon"><svg width="36" height="36" viewBox="0 0 36 36" fill="none" stroke="#fff" stroke-width="2.4" stroke-linecap="round"><path d="M30 18A12 12 0 1 1 18 6"/><path d="M22 4l-4 2 4 3M18 13v6l4 3M27 26l4 4"/></svg></div>
      <h3>État du marquage routier et mesure d'intensité</h3>
      <p>L'indicateur d'état est calculé à partir de l'intensité de réflexion du laser sur le marquage, offrant une évaluation précise et reproductible. Grâce au laser du lidar, nous mesurons précisément la position du marquage et l'indicateur d'intensité associé. Ces mesures sont agrégées par tronçon de 50m, permettant une évaluation détaillée de l'état du marquage routier. Cette approche offre des données 3D exploitables pour des études complémentaires, comme une vérification automatisée de la conformité des positions des bandes et des flèches de rabattement sur une route.</p>
    </article>
  </div>
</section>

<section class="benefits">
  <h2>Avantages De Notre Approche</h2>
  <div class="benefits-text"><p>Les images générées sont indépendantes des facteurs extérieurs comme la luminosité, assurant une reproductibilité de jour comme de nuit. La méthodologie garantit un score automatisé, éliminant la dépendance à des actions manuelles. Des données fiables et reproductibles renforcent la robustesse de la détection automatique des bandes, tandis que la précision centimétrique des relevés et des calculs de surfaces permet des estimations méticuleuses des métrés.</p></div>
  <div class="carousel">
    <figure class="slide">
      <div class="slide-visual" role="img" aria-label="Couche SIG avec tronçons colorés selon l'état de la chaussée" style="background:linear-gradient(135deg,#8a8a8a,#6f7a6c 40%,#9a7f6a 70%,#7c7c7c)"></div>
      <figcaption class="slide-caption">Couche SIG : état de la chaussée agrégé par tronçon</figcaption>
    </figure>
    <figure class="slide">
      <div class="slide-visual" role="img" aria-label="Plan de marquage en schéma itinéraire avec bandes et repères" style="background:linear-gradient(180deg,#ffffff,#f1f3fb 55%,#c8d0ef 70%,#f4f4f4)"></div>
      <figcaption class="slide-caption">Couche Plan de marquage sous forme de schéma itinéraire (largeurs de voies / PR) SIG : état de la chaussée agrégé par tronçon</figcaption>
    </figure>
    <figure class="slide">
      <div class="slide-visual" role="img" aria-label="Vectorisation des éléments de marquage au sol" style="background:linear-gradient(180deg,#ffffff,#fbf3f3 50%,#ffffff)"></div>
      <figcaption class="slide-caption">Vectorisation des éléments ponctuels et linéaires en vectoriel SIG / GeoDesk</figcaption>
    </figure>
  </div>
  <div class="carousel-arrow prev"><svg width="22" height="18" viewBox="0 0 22 18"><path d="M21 9H2M9 2 2 9l7 7" fill="none" stroke="#0b3310" stroke-width="2"/></svg></div>
  <div class="carousel-arrow next"><svg width="22" height="18" viewBox="0 0 22 18"><path d="M1 9h19M13 2l7 7-7 7" fill="none" stroke="#0b3310" stroke-width="2"/></svg></div>
</section>

<section class="studies">
  <h2 class="section-title">La Signalisation Horizontale Dans Nos Études</h2>
  <p class="studies-intro">En complément d'autres diagnostic d'éléments de voirie, ce diagnostic de la signalisation horizontale nous permet également, de réaliser des études de conformité plus complexes :</p>
  <div class="study-tiles">
    <div class="study-tile" role="img" aria-label="Vue lidar d'un passage piéton pour l'étude accessibilité" style="background:linear-gradient(180deg,#6c6c6c,#3d4a3e 55%,#109a2c)"><span>Accessibilité</span></div>
    <a class="study-tile" href="https://veltrane.example/etudes/intersection/" role="img" aria-label="Nuage de points d'une intersection en zone bâtie" style="background:linear-gradient(180deg,#1b1b1b,#5a5a5a 40%,#2a2a2a 65%,#0f8a28)"><span>Intersection</span></a>
    <div class="study-tile" role="img" aria-label="Nuage de points coloré d'une zone de stationnement et ralentisseurs" style="background:linear-gradient(160deg,#2a4bd8,#3a63e8 45%,#7a3fb0 60%,#15a23a)"><span>Stationnement &amp;<br>ralentisseurs</span></div>
    <div class="study-tile" role="img" aria-label="Nuage de points d'une route bordée de végétation" style="background:linear-gradient(180deg,#0c0c0c,#1f5a22 40%,#3a3a3a 60%,#10952b)"><span>Visibilité</span></div>
  </div>
</section>

<section class="importance">
  <h2 class="section-title">L'Importance Dela Signalisation Horizontale</h2>
  <div class="importance-cols">
    <div>
      <p>L'entretien de la signalisation horizontale est un aspect essentiel de la sécurité routière. En effet, les marquages au sol tels que les lignes de voie, les passages piétons et les flèches directionnelles, jouent un rôle crucial dans le guidage des conducteurs et des piétons sur les routes, il est donc important d'entretenir la signalisation horizontale pour assurer une circulation sûre et efficace.</p>
      <p>L'un des avantages clés de l'entretien régulier de la signalisation horizontale est l'amélioration de la visibilité et de l'orientation sur les routes. Les marquages clairs et bien entretenus permettent aux conducteurs de voir les lignes de voie, les passages piétons et les instructions de direction, même dans des conditions de conduite difficiles. Cela réduit les risques d'accidents dus à une mauvaise visibilité ou à une mauvaise compréhension des indications de la route.</p>
      <p>Cette maintenance est également essentielle pour garantir la conformité aux normes de sécurité routière. Les autorités en charge de la gestion des routes ont établi des règles et des directives strictes concernant les marquages au sol, et il est crucial de les respecter. Des marquages effacés, délavés ou incorrects peuvent entraîner une confusion chez les conducteurs, augmentant ainsi le risque d'accidents. En maintenant la signalisation horizontale en bon état, les autorités contribuent à la sécurité de tous les usagers de la route.</p>
    </div>
    <div>
      <p>Une signalisation horizontale bien entretenue permet d'optimiser la fluidité du trafic. Les lignes de voie clairement définies guident les conducteurs, réduisent les changements de voie inattendus et facilitent la circulation sur les routes. De plus, les flèches directionnelles précises aident les conducteurs à prendre rapidement les bonnes décisions aux intersections, évitant ainsi les embouteillages et les retards. Un trafic fluide contribue à une meilleure efficacité du transport et à une réduction des congestions routières.</p>
      <p>Investir dans l'entretien régulier de la signalisation horizontale est donc essentiel pour assurer une circulation sûre et harmonieuse sur nos routes.</p>
    </div>
  </div>
</section>

<section class="others">
  <h2 class="section-title">Nos Autres Post-Traitements</h2>
  <div class="others-list">
    <div class="other"><div class="other-visual" role="img" aria-label="Nuage de points coloré avec panneaux de signalisation verticale" style="background:linear-gradient(160deg,#2240c8,#3c66e6 50%,#6a3ab0 70%,#1e3fb8)"></div><span>Signalisation verticale</span></div>
    <div class="other"><div class="other-visual" role="img" aria-label="Plan technique des dispositifs de retenue avec légende" style="background:linear-gradient(180deg,#f6f6f6,#ffffff 50%,#ececec)"></div><span>Dispositif de retenue</span></div>
    <div class="other"><div class="other-visual" role="img" aria-label="Carte de l'état de la chaussée sur un tronçon routier" style="background:linear-gradient(135deg,#efefef,#d8d8d8 45%,#c9d86a 55%,#e6e6e6)"></div><span>Etat de la chaussée</span></div>
  </div>
</section>

<footer class="site-footer">
  <a class="footer-brand" href="https://veltrane.example/"><span class="brand-mark"></span><span class="brand-name">Veltrane</span></a>
  <div class="footer-cols">
    <div class="footer-col">
      <h4>Contact</h4>
      <ul>
        <li><svg width="14" height="16" viewBox="0 0 14 16"><path d="M7 15s5-5 5-9A5 5 0 0 0 2 6c0 4 5 9 5 9z" fill="none" stroke="#1ee83c" stroke-width="1.4"/><circle cx="7" cy="6" r="1.8" fill="none" stroke="#1ee83c" stroke-width="1.4"/></svg>12 rue des Tanneurs 94200 Ivry-Vallée</li>
        <li><svg width="14" height="14" viewBox="0 0 14 14"><path d="M3 1l2.5 3-1.5 1.5a8 8 0 0 0 4.5 4.5L10 8.5l3 2.5-1.5 2A11 11 0 0 1 1 2.5z" fill="none" stroke="#1ee83c" stroke-width="1.3"/></svg>contact@veltrane.example</li>
      </ul>
    </div>
    <div class="footer-col">
      <h4>Légal</h4>
      <ul><li>Mentions légales</li><li>Politique de confidentialité</li><li>Politique de cookies (UE)</li></ul>
    </div>
    <div class="footer-col">
      <h4>Navigation</h4>
      <div class="nav-split">
        <ul><li>Produit</li><li>Nos post-traitements</li><li>Nos clients</li></ul>
        <ul><li>Notre équipe</li><li>Contact</li></ul>
      </div>
    </div>
  </div>
</footer>
<div class="bottom-bar">© 2023 <em>Veltrane Work</em> - All Rights Reserved</div>

</body>
</html>
```